Velmar Ops Business Cards

We need to design some upbeat business cards. We are an Industrial Rope Access Company/Height Safety Company that specialize in Rope Access, Confined Space, Anchor Points, Safety Systems, PPE Inspecions and Rigging.
Company name is Velmar Ops Ltd
Card is for Gareth Lomas the Company Director
His mobile number is 027 418 9072 and email is gareth@velmarops.co.nz. Website address is www.velmarops.co.nz.
We will post some pictures below to ensure you get a good idea of what we do.

```html
<!DOCTYPE html>
<html lang="en">
<head>
<meta charset="utf-8">
<title>Velmar Ops Ltd – Business Card</title>
<link rel="stylesheet" href="https://fonts.googleapis.com/css2?family=Noto+Serif:ital,wght@0,700;1,700&display=swap">
<style>
  :root {
    --canvas-bg: #eef1f2;
    --card-white: #ffffff;
    --blue-deep: #2b8ff0;
    --blue-light: #5ad2fd;
    --photo-sky: #8f9291;
    --photo-mid: #6e716f;
    --photo-dark: #2c302d;
    --ink: #111111;
  }
  html, body {
    margin: 0;
    padding: 0;
    width: 1198px;
    height: 1200px;
    overflow: hidden;
    background: var(--canvas-bg);
  }
  .canvas {
    position: relative;
    width: 1198px;
    height: 1200px;
  }
  .card {
    position: absolute;
    left: 94px;
    width: 1010px;
    height: 536px;
    background: var(--card-white);
    box-shadow: 0 2px 6px rgba(0,0,0,0.12);
  }
  .card--front { top: 36px; }
  .card--back { top: 600px; }
  .card svg { display: block; width: 100%; height: 100%; }
  .company-name, .holder-title {
    font-family: "Noto Serif", Georgia, serif;
    font-weight: 700;
    font-style: italic;
    fill: var(--blue-deep);
  }
  .company-name { font-size: 40px; }
  .holder-title { font-size: 37px; }
  .contact-text {
    font-family: "Noto Serif", Georgia, serif;
    font-weight: 700;
    font-size: 22px;
    fill: var(--ink);
  }
  .band-deep { fill: var(--blue-deep); }
  .band-light { fill: var(--blue-light); }
  .rule { stroke: var(--blue-light); stroke-width: 4; }
  .icon-fill { fill: var(--blue-deep); }
  .icon-stroke { fill: none; stroke: var(--blue-deep); stroke-width: 2.5; }
</style>
</head>
<body>
<main class="canvas">

  <section class="card card--front" aria-label="Card front">
    <svg viewBox="0 0 1052 558" preserveAspectRatio="none">
      <defs>
        <linearGradient id="cityFront" x1="0" y1="0" x2="0" y2="1">
          <stop offset="0" stop-color="var(--photo-sky)"/>
          <stop offset="0.55" stop-color="var(--photo-mid)"/>
          <stop offset="1" stop-color="var(--photo-dark)"/>
        </linearGradient>
      </defs>
      <polygon role="img" aria-label="Photo of a city street lined with tall buildings"
        fill="url(#cityFront)" points="0,0 431,0 537,178 318,558 0,558"/>
      <polygon class="band-deep" points="431,0 564,0 601,68 537,178"/>
      <polygon class="band-light" points="601,68 624,106 366,558 318,558 537,178"/>
      <polygon class="band-deep" points="599,150 624,185 516,375 619,558 366,558"/>
      <rect x="626" y="272" width="40" height="40" class="band-light"/>
      <text class="company-name" x="703" y="313">Velmar Ops Ltd</text>
      <line class="rule" x1="687" y1="325" x2="981" y2="325"/>
    </svg>
  </section>

  <section class="card card--back" aria-label="Card back">
    <svg viewBox="0 0 1052 557" preserveAspectRatio="none">
      <defs>
        <linearGradient id="cityBack" x1="0" y1="0" x2="0" y2="1">
          <stop offset="0" stop-color="var(--photo-sky)"/>
          <stop offset="0.55" stop-color="var(--photo-mid)"/>
          <stop offset="1" stop-color="var(--photo-dark)"/>
        </linearGradient>
      </defs>
      <polygon role="img" aria-label="Photo of a city street lined with tall buildings"
        fill="url(#cityBack)" points="692,0 1052,0 1052,557 632,557 717,402 672,322 589,177"/>
      <polygon class="band-deep" points="559,0 692,0 589,177 522,67"/>
      <polygon class="band-light" points="522,67 475,147 577,322 445,557 540,557 672,322 589,177"/>
      <polygon class="band-deep" points="672,322 717,402 632,557 540,557"/>

      <text class="holder-title" x="42" y="127">Gareth Lomas Director</text>
      <line class="rule" x1="53" y1="145" x2="437" y2="145"/>

      <g class="contact-email">
        <rect x="54" y="276" width="39" height="25" class="icon-fill"/>
        <polyline points="54,277 73.5,291 93,277" fill="none" stroke="#fff" stroke-width="2"/>
        <text class="contact-text" x="124" y="295">gareth@velmarops.co.nz.</text>
      </g>
      <g class="contact-web">
        <circle cx="73" cy="358" r="18" class="icon-stroke"/>
        <ellipse cx="73" cy="358" rx="8" ry="18" class="icon-stroke" stroke-width="1.8"/>
        <line x1="55" y1="358" x2="91" y2="358" class="icon-stroke" stroke-width="1.8"/>
        <line x1="58" y1="349" x2="88" y2="349" class="icon-stroke" stroke-width="1.5"/>
        <line x1="58" y1="367" x2="88" y2="367" class="icon-stroke" stroke-width="1.5"/>
        <text class="contact-text" x="124" y="365">www.velmarops.co.nz.</text>
      </g>
      <g class="contact-phone">
        <path class="icon-fill" d="M58 414 l7-6 l9 11 l-5 5 q5 10 14 16 l5-5 l10 9 l-6 7 q-22-6-34-37z"/>
        <text class="contact-text" x="149" y="433">027 418 9072</text>
      </g>
    </svg>
  </section>

</main>
</body>
</html>
```